Badgerline Custom Woodcraft Website design

Need a small website to showcase my products and take orders

would also like payment options

We do custom wood work along with cnc work in wood plastic and soft metals

we are based in edmonton alberta canada
Updates

Industry/Entity Type

Work

Number of Pages Required

3 page

Requirements
Nice to have
• Interview for for a woodworking magazine
• http://timberquarterlyexample.com/issue-1-02-august-2016/member-spotlight
• I would also like to see metal working/branding iron info
• Also adding the picture of me from the above interview is a nice touch

```html
<!DOCTYPE html>
<html lang="en">
<head>
<meta charset="utf-8">
<title>Badgerline Custom Woodcraft</title>
<link rel="stylesheet" href="https://fonts.googleapis.com/css2?family=Cinzel:wght@400;700&family=Arimo:wght@400;700&family=Roboto:wght@400;500&display=swap">
<style>
:root{
  --cream:#f0dcc7;
  --cream-soft:#efd9c3;
  --brown:#5a4535;
  --brown-deep:#4e3b2d;
  --tan:#b8906e;
  --tan-light:#c9a27f;
  --accent:#b38a66;
  --ink:#3d2c20;
  --text:#5b4a3d;
  --white:#ffffff;
}
*{margin:0;padding:0;box-sizing:border-box}
html,body{width:1200px;height:2597px;overflow:hidden}
body{position:relative;background:var(--cream);font-family:"Arimo",Arial,sans-serif;color:var(--text)}

/* header */
.site-header{position:absolute;left:0;top:0;width:1200px;height:146px;background:var(--cream)}
.call{position:absolute;left:78px;top:46px;display:flex;align-items:center;gap:18px}
.call-label{font-family:"Roboto",Arial,sans-serif;font-size:16px;color:var(--ink)}
.call-number{font-family:"Roboto",Arial,sans-serif;font-weight:500;font-size:27px;color:var(--ink);line-height:1.1}
.brand{position:absolute;left:450px;top:12px;width:300px;text-align:center}
.brand-dot{width:80px;height:80px;border-radius:50%;background:var(--tan-light);margin:0 auto 6px}
.brand-name{font-family:"Cinzel",Georgia,serif;font-weight:700;font-size:19px;line-height:1.05;color:var(--ink);letter-spacing:1px}
.pill{position:absolute;display:flex;align-items:center;justify-content:space-between;background:var(--brown);color:var(--white);border-radius:30px;font-family:"Cinzel",Georgia,serif;padding-left:26px;white-space:nowrap}
.pill .knob{width:50px;height:50px;border-radius:50%;background:var(--cream);border:3px solid var(--tan-light);margin-right:3px;flex:none}
.pill-pay{left:935px;top:47px;width:187px;height:55px;font-size:20px}

/* nav */
.main-nav{position:absolute;left:0;top:146px;width:1200px;height:64px;background:var(--brown)}
.main-nav a{position:absolute;top:0;height:64px;line-height:64px;color:var(--white);text-decoration:none;font-family:"Cinzel",Georgia,serif;font-size:18px;transform:translateX(-50%)}
.main-nav a.active{background:var(--tan);width:104px;text-align:center}

/* hero */
.hero{position:absolute;left:0;top:210px;width:1200px;height:476px;background:linear-gradient(100deg,#6d4a33 0%,#a9744f 30%,#8a5a3a 55%,#c79a72 75%,#5d3e2b 100%);box-shadow:0 14px 22px rgba(60,40,25,.35)}
.hero-title{position:absolute;left:0;top:133px;width:1200px;text-align:center;color:var(--white);font-family:"Cinzel",Georgia,serif;font-weight:700;font-size:56px;line-height:70px;letter-spacing:2px}
.hero-arrow{position:absolute;top:207px;width:52px;height:52px;border-radius:50%;border:2px solid var(--brown-deep)}
.pill-hero{left:430px;top:283px;width:332px;height:64px;font-size:22px;padding-left:40px}
.pill-hero .knob{width:58px;height:58px}

/* welcome */
.coin{position:absolute;left:78px;top:748px;width:324px;height:288px;border-radius:50%;background:radial-gradient(circle,#7a5a44 0%,#5b4131 60%,#3e2c21 100%)}
.welcome-text{position:absolute;left:449px;top:748px;width:680px}
.eyebrow{font-size:19px;color:var(--accent);letter-spacing:.5px}
.section-title{font-family:"Cinzel",Georgia,serif;font-weight:700;font-size:31px;color:var(--ink);letter-spacing:1px}
.welcome-text .section-title{margin-top:14px}
.welcome-text p{font-size:14.5px;line-height:27.5px;color:var(--text)}
.pill-more{left:450px;top:989px;width:229px;height:56px;font-size:21px}

/* products */
.products{position:absolute;left:0;top:1108px;width:1200px;height:657px;background:var(--brown)}
.products .eyebrow{position:absolute;top:62px;width:1200px;text-align:center;color:var(--tan-light)}
.products .section-title{position:absolute;top:98px;width:1200px;text-align:center;color:var(--white);font-size:34px}
.card{position:absolute;top:156px;width:332px;height:438px;background:var(--tan)}
.card-media{position:absolute;left:0;top:0;width:332px;height:253px;background:var(--cream-soft);overflow:hidden}
.card-media .shape{position:absolute;left:40px;top:20px;width:252px;height:210px;background:linear-gradient(160deg,#d9b289,#b98a60);border-radius:14px}
.card-media .shape.oval{left:28px;top:60px;width:276px;height:150px;border-radius:50%}
.card-corner{position:absolute;right:0;top:0;width:0;height:0;border-left:84px solid transparent;border-top:84px solid var(--tan)}
.cart{position:absolute;right:12px;top:10px}
.card-name{position:absolute;top:272px;width:332px;text-align:center;font-family:"Cinzel",Georgia,serif;font-size:20px;color:var(--ink)}
.card-price{position:absolute;top:308px;width:332px;text-align:center;font-size:33px;color:var(--white)}
.pill-order{left:52px;top:362px;width:228px;height:56px;font-size:20px}

/* contact */
.contact-head{position:absolute;left:0;top:1824px;width:1200px;text-align:center}
.contact-head .section-title{margin-top:10px;font-size:34px}
.contact-head p{width:860px;margin:18px auto 0;font-size:14.5px;line-height:26px}
.field{position:absolute;background:var(--white);font-size:14px;color:#6b5b4f;padding:14px 12px}
.pill-submit{left:506px;top:2158px;width:187px;height:56px;font-size:21px}

/* footer */
.site-footer{position:absolute;left:0;top:2274px;width:1200px;height:323px;background:var(--brown);color:var(--white)}
.foot-col{position:absolute;top:34px}
.foot-col h4{font-family:"Roboto",Arial,sans-serif;font-weight:500;font-size:16px;margin-bottom:20px}
.links li{list-style:none;font-size:14px;line-height:29px}
.links li::before{content:"»";margin-right:10px;color:var(--tan-light)}
.touch-row{display:flex;gap:18px;font-size:13.5px;line-height:22px;margin-bottom:10px;color:#e9d8c6}
.touch-row b{color:var(--white)}
.news-text{font-size:13.5px;line-height:24px;color:#e0cbb6;width:210px}
.news-input{margin-top:10px;width:240px;height:46px;border:1px solid var(--tan-light);border-radius:24px;font-size:13.5px;color:#d8c2ac;padding:14px 18px}
.pill-sub{left:610px;top:2454px;width:190px;height:46px;background:var(--tan);font-size:18px;padding-left:26px}
.pill-sub .knob{width:40px;height:40px}
.foot-brand{position:absolute;left:930px;top:30px;width:120px;height:120px;border-radius:50%;background:var(--cream);display:flex;align-items:center;justify-content:center;text-align:center;font-family:"Cinzel",Georgia,serif;font-weight:700;font-size:13px;color:var(--ink);line-height:1.2}
.foot-rule{position:absolute;left:883px;top:168px;width:222px;height:1px;background:#7a6352}
.social{position:absolute;top:180px;width:48px;height:48px;border-radius:50%;border:1.5px solid #8b735f}
.social.filled{background:var(--tan)}
.foot-divider{position:absolute;left:78px;top:254px;width:1044px;height:1px;background:#6a5444}
.copyright{position:absolute;top:283px;width:1200px;text-align:center;font-size:14px;color:var(--tan-light)}
.copyright b{font-weight:400;color:var(--white)}
</style>
</head>
<body>

<header class="site-header">
  <div class="call">
    <svg width="34" height="34" viewBox="0 0 24 24" aria-hidden="true"><path fill="#5a4535" d="M6.6 10.8a15.1 15.1 0 0 0 6.6 6.6l2.2-2.2a1 1 0 0 1 1-.25 11.4 11.4 0 0 0 3.6.57 1 1 0 0 1 1 1V20a1 1 0 0 1-1 1A17 17 0 0 1 3 4a1 1 0 0 1 1-1h3.5a1 1 0 0 1 1 1c0 1.25.2 2.45.57 3.57a1 1 0 0 1-.25 1z"/></svg>
    <div>
      <div class="call-label">Call Us Now</div>
      <div class="call-number">780-555-0142</div>
    </div>
  </div>
  <div class="brand">
    <div class="brand-dot"></div>
    <div class="brand-name">BADGERLINE<br>CUSTOM WOODCRAFT</div>
  </div>
  <a class="pill pill-pay">PAYMENT<span class="knob"></span></a>
</header>

<nav class="main-nav">
  <a class="active" style="left:322px">HOME</a>
  <a style="left:450px">ABOUT</a>
  <a style="left:590px">PRODUCT</a>
  <a style="left:725px">NEWS</a>
  <a style="left:860px">CONTACT</a>
</nav>

<section class="hero" role="img" aria-label="Hand plane on a workbench among curled wood shavings">
  <h1 class="hero-title">BADGERLINE CUSTOM<br>WOODCRAFT</h1>
  <span class="hero-arrow" style="left:12px">
    <svg width="48" height="48" viewBox="0 0 48 48" aria-hidden="true"><path d="M28 15l-9 9 9 9" fill="none" stroke="#4e3b2d" stroke-width="2.5"/></svg>
  </span>
  <span class="hero-arrow" style="left:1134px">
    <svg width="48" height="48" viewBox="0 0 48 48" aria-hidden="true"><path d="M20 15l9 9-9 9" fill="none" stroke="#4e3b2d" stroke-width="2.5"/></svg>
  </span>
  <a class="pill pill-hero">CONTACT US KNOW<span class="knob"></span></a>
</section>

<section class="welcome">
  <div class="coin" role="img" aria-label="Carved wooden medallion with engraved lettering"></div>
  <div class="welcome-text">
    <div class="eyebrow">WELCOME TO</div>
    <h2 class="section-title">BADGERLINE CUSTOM WOODCRAFT</h2>
    <p style="margin-top:14px">Lorem Ipsum is simply dummy text of the printing and typesetting industry. Lorem Ipsum has been the industry's standard dummy text ever since the 1500s, when an unknown printer took a galley of type and scrambled it to make a type specimen book. It has survived not only five</p>
    <p style="margin-top:4px">It was popularised in the 1960s with the release of Tamworth Press sheets containing Lorem Ipsum passages, and more recently with desktop publishing software like Quillset Layout .</p>
  </div>
  <a class="pill pill-more">KNOW MORE<span class="knob"></span></a>
</section>

<section class="products">
  <div class="eyebrow">WHAT WE PROVIDE</div>
  <h2 class="section-title">OUR PRODUCT</h2>

  <article class="card" style="left:78px">
    <div class="card-media"><div class="shape" role="img" aria-label="Folding wooden stool"></div><div class="card-corner"></div>
      <svg class="cart" width="30" height="28" viewBox="0 0 30 28" aria-hidden="true"><path d="M2 3h5l3 14h14l3-10H9" fill="none" stroke="#fff" stroke-width="2"/><circle cx="12" cy="23" r="2" fill="#fff"/><circle cx="22" cy="23" r="2" fill="#fff"/></svg></div>
    <div class="card-name">PRODUCT NAME</div>
    <div class="card-price">$299.49</div>
    <a class="pill pill-order">ODER KNOW<span class="knob"></span></a>
  </article>

  <article class="card" style="left:433px">
    <div class="card-media"><div class="shape" role="img" aria-label="Folding wooden chair"></div><div class="card-corner"></div>
      <svg class="cart" width="30" height="28" viewBox="0 0 30 28" aria-hidden="true"><path d="M2 3h5l3 14h14l3-10H9" fill="none" stroke="#fff" stroke-width="2"/><circle cx="12" cy="23" r="2" fill="#fff"/><circle cx="22" cy="23" r="2" fill="#fff"/></svg></div>
    <div class="card-name">PRODUCT NAME</div>
    <div class="card-price">$499.39</div>
    <a class="pill pill-order">ODER KNOW<span class="knob"></span></a>
  </article>

  <article class="card" style="left:790px">
    <div class="card-media"><div class="shape oval" role="img" aria-label="Carved oval wooden board"></div><div class="card-corner"></div>
      <svg class="cart" width="30" height="28" viewBox="0 0 30 28" aria-hidden="true"><path d="M2 3h5l3 14h14l3-10H9" fill="none" stroke="#fff" stroke-width="2"/><circle cx="12" cy="23" r="2" fill="#fff"/><circle cx="22" cy="23" r="2" fill="#fff"/></svg></div>
    <div class="card-name">PRODUCT NAME</div>
    <div class="card-price">$699.29</div>
    <a class="pill pill-order">ODER KNOW<span class="knob"></span></a>
  </article>
</section>

<section class="contact">
  <div class="contact-head">
    <div class="eyebrow">GET IN TOUCH</div>
    <h2 class="section-title">CONTACT US</h2>
    <p>Lorem Ipsum is simply dummy text of the printing and typesetting industry. Lorem Ipsum has been the industry's standard dummy text ever since the 1500s, when an unknown printer took.</p>
  </div>
  <div class="field" style="left:154px;top:1979px;width:291px;height:49px">Name*</div>
  <div class="field" style="left:455px;top:1979px;width:290px;height:49px">Email*</div>
  <div class="field" style="left:755px;top:1979px;width:291px;height:49px">Phone*</div>
  <div class="field" style="left:154px;top:2040px;width:892px;height:102px">Message*</div>
  <a class="pill pill-submit">SUBMIT<span class="knob"></span></a>
</section>

<footer class="site-footer">
  <div class="foot-col" style="left:78px">
    <h4>USEFULL LINKS</h4>
    <ul class="links"><li>Home</li><li>About</li><li>Product</li><li>News</li><li>Contact</li></ul>
  </div>
  <div class="foot-col" style="left:343px">
    <h4>GET IN TOUCH</h4>
    <div class="touch-row">
      <svg width="16" height="20" viewBox="0 0 16 20" aria-hidden="true"><path d="M8 1a6 6 0 0 0-6 6c0 5 6 12 6 12s6-7 6-12a6 6 0 0 0-6-6z" fill="none" stroke="#c9a27f" stroke-width="1.5"/><circle cx="8" cy="7" r="2" fill="none" stroke="#c9a27f" stroke-width="1.5"/></svg>
      <div><b>Badgerline Custom Woodcraft</b><br>Lorem ipsum dolor amet simple.</div>
    </div>
    <div class="touch-row">
      <svg width="16" height="18" viewBox="0 0 24 24" aria-hidden="true"><path d="M6.6 10.8a15.1 15.1 0 0 0 6.6 6.6l2.2-2.2a1 1 0 0 1 1-.25 11.4 11.4 0 0 0 3.6.57 1 1 0 0 1 1 1V20a1 1 0 0 1-1 1A17 17 0 0 1 3 4a1 1 0 0 1 1-1h3.5a1 1 0 0 1 1 1c0 1.25.2 2.45.57 3.57a1 1 0 0 1-.25 1z" fill="none" stroke="#c9a27f" stroke-width="1.8"/></svg>
      <div>780 555 0142</div>
    </div>
    <div class="touch-row">
      <svg width="16" height="18" viewBox="0 0 16 16" aria-hidden="true"><rect x="4" y="1.5" width="8" height="4" fill="none" stroke="#c9a27f"/><rect x="1.5" y="5.5" width="13" height="6" fill="none" stroke="#c9a27f"/><rect x="4" y="9.5" width="8" height="5" fill="none" stroke="#c9a27f"/></svg>
      <div>780 555 0142</div>
    </div>
    <div class="touch-row">
      <svg width="16" height="18" viewBox="0 0 16 16" aria-hidden="true"><rect x="1" y="3" width="14" height="10" fill="none" stroke="#c9a27f" stroke-width="1.3"/><path d="M1 3l7 6 7-6" fill="none" stroke="#c9a27f" stroke-width="1.3"/></svg>
      <div>info@badgerlinewood.com</div>
    </div>
  </div>
  <div class="foot-col" style="left:610px">
    <h4>NEWSLETTER</h4>
    <p class="news-text">Subscribe to stay on Badgerline Custom Woodcraft</p>
    <div class="news-input" style="margin-left:-4px">Enter your Email</div>
  </div>
  <div class="foot-brand">Badgerline<br>Custom<br>Woodcraft</div>
  <div class="foot-rule"></div>
  <span class="social filled" style="left:913px" aria-label="Social link"></span>
  <span class="social" style="left:968px" aria-label="Social link"></span>
  <span class="social" style="left:1024px" aria-label="Social link"></span>
  <div class="foot-divider"></div>
  <div class="copyright">©<b>Badgerline Custom Woodcraft</b> - 2016 All rights reserved.</div>
</footer>
<a class="pill pill-sub">SUBSCRIBE<span class="knob"></span></a>

</body>
</html>
```